Slides for industrial furniture site

I am looking for three slides (1400x530) that will go on my homepage. All slides need to be simple and a projection of the goods i am selling.
The slides need to be up there in the design trends for 2014.
I prefer:
- One large photo in each slide, maybe faded with a product in the front.
- Some example text in different fonts.
- light coloured slides. That go well in white oriented site.
- pictures may include these products: https://www.findora-example.nl/search?q=morvane+lights
AND:
https://www.findora-example.nl/search?q=vintage+theatre+light
OR:
https://www.findora-example.nl/search?q=vintage+stools
OR:
https://www.findora-example.nl/search?q=brevak+chair#q=original%20brevak%20chair
Maybe one slide with an interior like this:
https://www.findora-example.nl/search?q=industrial+interiors
Just let me see your creations and take into account the above.
For some examples:
http://quietmarsh-example.co/
http://pixelhof-example.at/en/
https://www.fernandlamp-example.com/
http://www.ulvastudio-example.com/
http://quillbarrow-example.ca/en/
http://skinforge-example.com/
For some theory (sorry if this is offensive ;-):
http://www.deckvault-example.net/plumo/font-pairing-slides
http://www.deckvault-example.net/brightmill2014/web-design-trends-2014
http://www.deckvault-example.net/tobyrand/how-to-create-great-slides-for-presentations
I hope you can create great slides for me!
Thnx
Reason: Hi designers. I am still looking for the perfect three lsides. Could you please make a few more.
Greetings,
Harlem
Reason: Sorry designers.
I am waiting for some designs from specific designers.
Industrial

```html
<!DOCTYPE html>
<html lang="en">
<head>
<meta charset="utf-8">
<title>Live from 1 October – Industrial lights</title>
<link rel="stylesheet" href="https://fonts.googleapis.com/css2?family=Bebas+Neue&family=Lobster&display=swap">
<style>
  :root {
    --wall-light: #c3c9c5;
    --wall-mid: #a9b0ac;
    --wall-dark: #8f9692;
    --white: #ffffff;
    --ink: #000000;
    --control: rgba(255, 255, 255, 0.75);
  }
  html, body {
    margin: 0;
    padding: 0;
    width: 1200px;
    height: 454px;
    overflow: hidden;
    background: var(--white);
  }
  .slide {
    position: relative;
    width: 1200px;
    height: 454px;
    overflow: hidden;
  }
  .slide-photo {
    position: absolute;
    inset: 0;
    background:
      radial-gradient(ellipse 260px 200px at 300px 120px, rgba(110,116,114,0.55), transparent 70%),
      linear-gradient(100deg, var(--wall-mid) 0%, var(--wall-light) 45%, var(--wall-mid) 80%, var(--wall-dark) 100%);
  }
  .headline-frame {
    position: absolute;
    left: 187px;
    top: 92px;
    width: 823px;
    height: 175px;
    border: 4px solid var(--white);
    display: flex;
    align-items: center;
    justify-content: center;
  }
  .headline {
    margin: 0;
    padding-top: 10px;
    font-family: "Bebas Neue", "Oswald", sans-serif;
    font-weight: 400;
    font-size: 118px;
    line-height: 1;
    letter-spacing: 1px;
    color: var(--white);
    white-space: nowrap;
  }
  .tagline {
    position: absolute;
    left: 278px;
    top: 291px;
    width: 589px;
    height: 63px;
    background: var(--ink);
    display: flex;
    align-items: center;
    justify-content: center;
    margin: 0;
    font-family: "Lobster", cursive;
    font-weight: 400;
    font-size: 41px;
    line-height: 1;
    color: var(--white);
  }
  .nav-arrow {
    position: absolute;
    top: 208px;
    width: 36px;
    height: 44px;
  }
  .nav-arrow--prev { left: 32px; }
  .nav-arrow--next { left: 1136px; }
  .pager {
    position: absolute;
    top: 411px;
    left: 569px;
    display: flex;
    gap: 15px;
  }
  .pager-dot {
    width: 15px;
    height: 15px;
    border-radius: 50%;
    background: rgba(255,255,255,0.6);
  }
  .pager-dot--active { background: var(--white); }
</style>
</head>
<body>
  <section class="slide">
    <div class="slide-photo" role="img" aria-label="Photo of a brushed steel industrial wall lamp with an articulated arm against a grey painted plank wall"></div>

    <div class="headline-frame">
      <h1 class="headline">Live from 1 October</h1>
    </div>

    <p class="tagline">See all our industrial lights!</p>

    <svg class="nav-arrow nav-arrow--prev" viewBox="0 0 36 44" aria-label="Previous slide">
      <polyline points="28,6 10,22 28,38" fill="none" stroke="var(--control)" stroke-width="8"/>
    </svg>
    <svg class="nav-arrow nav-arrow--next" viewBox="0 0 36 44" aria-label="Next slide">
      <polyline points="8,6 26,22 8,38" fill="none" stroke="var(--control)" stroke-width="8"/>
    </svg>

    <div class="pager">
      <span class="pager-dot pager-dot--active"></span>
      <span class="pager-dot"></span>
      <span class="pager-dot"></span>
    </div>
  </section>
</body>
</html>
```